2367 Halvorsen Avenue Medical Centre

We are looking for a design for new medical clinic.
We are accepting new patients at this new medical centre grand opening. Walk-ins are welcome.
Our cardiac and vascular surgical specialists are department heads at St Alder's Hospital, a leading teaching hospital in Toronto. These specialists will see cardiovascular consults are well as pre-surgical and post-surgical consultations and follow-ups.
Our lab is affiliated with several nuclear medicine clinics in the GTA.
Our Services Includes:
Family Practice
Cardiology Diagnostics
Cardiac & Vascular Surgical Consultation
Ultrasound & Vascular Testing
Open 6 days a week.
Ample Free Parking
Friendly Staffs

Target Market(s)

New Patients. Families of any age. Ethnic groups including Asians & Africans.

Industry/Entity Type

Medical

Font styles to use
Serif
Sans Serif
Decorative
Script
Other font styles liked:
• Arial calibri, verdana

Requirements
Must have
• Address:
• 2367 Halvorsen Avenue East
• Unit 225
• Scarborough, Ontario
• K7T 2P4
• Tel: (416) 555-0148
Nice to have
• Caring and inviting environment.
• Simple but classy.
• Standout colors.
Should not have
• Busy images. Aside from this, any ideas are welcome.

```html
<!DOCTYPE html>
<html lang="en">
<head>
<meta charset="utf-8">
<title>2367 Halvorsen Avenue Medical Centre – Grand Opening</title>
<link href="https://fonts.googleapis.com/css2?family=Great+Vibes&family=Open+Sans:wght@400;600;700&family=Roboto+Condensed:wght@700&family=Arimo:wght@700&family=Courgette&family=Lato:wght@400&display=swap" rel="stylesheet">
<style>
  :root{
    --green-light:#a6d64a;
    --green:#7cc142;
    --blue:#1673c0;
    --blue-dark:#0d5fae;
    --teal:#2bb3c8;
    --cyan:#27b7e0;
    --pink:#e8246f;
    --pink-light:#f0508a;
    --yellow:#fff200;
    --yellow-edge:#f3c400;
    --navy:#2a3990;
    --ink:#111;
    --grey-text:#555;
    --paper:#f3f3f4;
    --white:#fff;
  }
  *{box-sizing:border-box;margin:0;padding:0}
  html,body{width:975px;height:1200px;overflow:hidden;background:#e9e9e9}
  .flyer{position:relative;width:975px;height:1200px;background:var(--paper);overflow:hidden;font-family:'Open Sans',sans-serif}
  .backdrop{position:absolute;inset:0}
  .photo{position:absolute;left:0;top:80px;width:275px;height:500px;
    background:linear-gradient(180deg,#e6c3b0 0%,#d8a990 30%,#7fd0d6 55%,#3bb3c3 100%);
    clip-path:ellipse(100% 100% at 0% 0%);opacity:.9}
  .grand{position:absolute;left:262px;top:40px;width:631px;text-align:center;font-family:'Great Vibes',cursive;font-size:112px;color:var(--white);text-shadow:2px 3px 4px rgba(0,0,0,.35);line-height:1.2;white-space:nowrap}
  .title{position:absolute;left:231px;top:224px;width:700px;text-align:center;font-family:'Arimo',sans-serif;font-weight:700;color:var(--white);font-size:94px;line-height:102px;letter-spacing:-3px;white-space:nowrap;text-shadow:2px 4px 5px rgba(0,0,0,.35)}
  .address{position:absolute;left:320px;top:452px;width:520px;text-align:center;font-weight:600;font-size:30px;line-height:45px;color:var(--ink);white-space:nowrap}
  .lab-badge{position:absolute;left:42px;top:484px;width:192px;height:192px;border-radius:50%;
    background:radial-gradient(circle at 40% 35%,#fff 55%,#e4e6ea 100%);box-shadow:0 4px 8px rgba(0,0,0,.35);
    display:flex;align-items:center;justify-content:center;text-align:center;color:var(--navy);font-weight:600;font-size:18px;line-height:26px}
  .walkin-badge{position:absolute;left:229px;top:592px;width:248px;height:248px;border-radius:50%;border:5px solid var(--white);
    background:radial-gradient(circle at 35% 30%,var(--pink-light) 0%,var(--pink) 60%,#d01560 100%);box-shadow:0 4px 10px rgba(0,0,0,.35);
    display:flex;align-items:center;justify-content:center;text-align:center;font-family:'Roboto Condensed',sans-serif;font-weight:700;color:var(--white);font-size:46px;line-height:52px;text-shadow:1px 2px 3px rgba(0,0,0,.35)}
  .open-tag{position:absolute;left:494px;top:605px;width:421px;height:240px}
  .open-text{position:absolute;left:545px;top:662px;width:330px;text-align:center;transform:rotate(-12deg);font-family:'Roboto Condensed',sans-serif;font-weight:700;font-size:52px;line-height:54px;color:var(--ink);white-space:nowrap}
  .specialists{position:absolute;left:40px;top:682px;font-family:'Lato',sans-serif;font-size:12.5px;line-height:19.3px;color:var(--grey-text);white-space:nowrap}
  .services-head{position:absolute;left:0;top:881px;width:350px;height:35px;background:var(--cyan);border-radius:0 10px 10px 0;
    color:var(--white);font-weight:600;font-size:23px;line-height:35px;padding-left:42px;white-space:nowrap}
  .services{position:absolute;left:51px;top:926px;list-style:none;font-size:19.5px;line-height:25px;color:#222;white-space:nowrap}
  .services li{position:relative;padding-left:18px;margin-bottom:7px}
  .services li::before{content:"";position:absolute;left:-6px;top:6px;width:13px;height:13px;border-radius:50%;background:var(--pink)}
  .welcome{position:absolute;right:45px;top:866px;font-family:'Courgette',cursive;font-size:45px;line-height:60px;color:var(--pink);font-style:italic;white-space:nowrap}
  .call{position:absolute;right:49px;top:948px;text-align:right;font-family:'Roboto Condensed',sans-serif;font-weight:700;font-size:62px;line-height:55px;color:var(--blue);white-space:nowrap}
  .phone{position:absolute;left:475px;top:1076px;width:500px;height:81px;background:linear-gradient(180deg,#1f86d4,var(--blue-dark));
    border-radius:40px 0 0 40px;box-shadow:0 3px 6px rgba(0,0,0,.3);color:var(--white);font-family:'Roboto Condensed',sans-serif;font-weight:700;font-size:66px;line-height:81px;padding-left:48px;white-space:nowrap;text-shadow:1px 2px 3px rgba(0,0,0,.35)}
</style>
</head>
<body>
<div class="flyer">
  <svg class="backdrop" width="975" height="1200" viewBox="0 0 975 1200" aria-hidden="true">
    <defs>
      <linearGradient id="greenFill" x1="0" y1="0" x2="1" y2="1">
        <stop offset="0" stop-color="#b3dc52"/>
        <stop offset="1" stop-color="#6cb83c"/>
      </linearGradient>
      <linearGradient id="blueFill" x1="0" y1="0" x2="1" y2="1">
        <stop offset="0" stop-color="#0d5fae"/>
        <stop offset="1" stop-color="#1e8fd6"/>
      </linearGradient>
    </defs>
    <path d="M0 0 H975 V650 Q800 780 520 770 Q300 760 150 640 Q40 560 0 480 Z" fill="url(#blueFill)"/>
    <path d="M150 0 H975 V640 Q800 760 520 752 Q330 745 250 620 Q140 430 190 200 Q210 80 250 0 Z" fill="url(#greenFill)"/>
    <path d="M180 0 Q100 160 110 330" fill="none" stroke="#7fd3e0" stroke-width="10"/>
    <path d="M160 0 Q80 160 90 330" fill="none" stroke="var(--teal)" stroke-width="14"/>
    <path d="M0 500 Q120 700 330 760 Q420 785 520 772" fill="none" stroke="#9fd8ef" stroke-width="6"/>
  </svg>

  <div class="photo" role="img" aria-label="Photo of a smiling nurse in teal scrubs with a stethoscope holding a clipboard"></div>

  <div class="grand">Grand Opening</div>
  <h1 class="title">NEW MEDICAL<br>CLINIC</h1>
  <p class="address">2367 Halvorsen Avenue East,<br>Unit 225, Scarborough,<br>Ontario, K7T 2P4</p>

  <div class="lab-badge"><p>Our lab is<br>affiliated with<br>several nuclear<br>medicine clinics<br>in the GTA.</p></div>

  <p class="specialists">Our cardiac and vascular<br>surgical specialists are<br>department heads at St<br>Alder's Hospital, a leading<br>teaching hospital in Toronto.<br>These specialists will see<br>cardiovascular consults are well as<br>pre-surgical and post-surgical<br>consultations and follow-ups.</p>

  <div class="walkin-badge"><p>Accepting<br>Walk-in<br>Patients</p></div>

  <svg class="open-tag" viewBox="0 0 421 240" aria-hidden="true">
    <path d="M30 140 Q20 80 110 60 Q250 20 350 40 Q405 55 395 120 Q385 190 260 200 Q120 215 60 195 Q35 180 30 140 Z" fill="var(--yellow)" stroke="var(--yellow-edge)" stroke-width="3"/>
    <path d="M15 150 Q5 70 120 48 Q270 10 370 30 Q415 45 405 125" fill="none" stroke="var(--yellow-edge)" stroke-width="2"/>
    <path d="M395 110 Q390 205 250 215 Q100 228 40 200 Q10 180 20 130" fill="none" stroke="var(--yellow-edge)" stroke-width="2"/>
  </svg>
  <p class="open-text">OPEN 6 DAYS<br>A WEEK</p>

  <h2 class="services-head">Our Services Includes:</h2>
  <ul class="services">
    <li>Family Practice</li>
    <li>Cardiology Diagnostics</li>
    <li>Cardiac &amp; Vascular Surgical<br>Consultation</li>
    <li>Ultrasound &amp; Vascular Testing</li>
    <li>Open 6 days a week.</li>
    <li>Ample Free Parking</li>
    <li>Friendly Staffs</li>
  </ul>

  <p class="welcome">Walk-ins are Welcome</p>
  <p class="call">CALL FOR BOOK<br>APPOINTMENT</p>
  <p class="phone">(416) 555-0148</p>
</div>
</body>
</html>
```